Australian IT Company New Logo Business Cards Required

We are a computer consultancy / MSP located in Brisbane Australia looking to have business cards designed with our new logo, we are looking for something professional that catches the eye.
I can provide the logo in other formats if required, let's see what you can create!

```html
<!DOCTYPE html>
<html lang="en">
<head>
<meta charset="utf-8">
<title>Verdanet Business Cards</title>
<link rel="stylesheet" href="https://fonts.googleapis.com/css2?family=Open+Sans:wght@400;600;700;800&display=swap">
<style>
  :root {
    --brand-green: #84bf41;
    --paper: #f4f4f4;
    --ink: #2b2b2b;
    --muted-grey: #7a7a7a;
    --white: #ffffff;
    --backdrop: #e4e4e4;
  }
  * { margin: 0; padding: 0; box-sizing: border-box; }
  html, body {
    width: 1200px; height: 960px; overflow: hidden;
    background: var(--backdrop);
    font-family: "Open Sans", Arial, sans-serif;
  }
  .canvas { position: relative; width: 1200px; height: 960px; }
  .card {
    position: absolute; left: 311px; width: 579px; height: 354px;
    overflow: hidden;
  }
  .card--front { top: 106px; background: var(--brand-green); color: var(--white); }
  .card--back { top: 506px; background: var(--paper); color: var(--ink); }

  .brand-name {
    position: absolute; font-weight: 800; letter-spacing: 0.5px; line-height: 1;
  }
  .tagline {
    position: absolute; font-weight: 700; letter-spacing: 0.9px; line-height: 1;
  }
  .card--front .brand-name { left: 0; right: 0; top: 150px; text-align: center; font-size: 52px; }
  .card--front .tagline { left: 0; right: 0; top: 204px; text-align: center; font-size: 15.5px; }
  .card--front .website {
    position: absolute; left: 0; right: 0; top: 307px; text-align: center;
    font-size: 13.5px; letter-spacing: 1px;
  }

  .card--back .brand-name { left: 40px; top: 54px; font-size: 44px; color: var(--brand-green); }
  .card--back .tagline { left: 41px; top: 111px; font-size: 13px; color: var(--muted-grey); }

  .address { position: absolute; left: 41px; top: 204px; font-size: 13.5px; line-height: 19px; }
  .contact-list { position: absolute; left: 41px; top: 258px; list-style: none; font-size: 13.5px; line-height: 19.5px; }
  .contact-list li { display: flex; align-items: center; gap: 5px; }
  .contact-list svg { width: 13px; height: 13px; flex: none; }

  .corner-shape { position: absolute; left: 0; top: 0; }
  .person { position: absolute; right: 12px; top: 274px; text-align: right; color: var(--white); }
  .person__name { font-size: 16.5px; font-weight: 700; line-height: 20px; }
  .person__role { font-size: 13.5px; line-height: 19px; }
</style>
</head>
<body>
<main class="canvas">
  <section class="card card--front" aria-label="Card front">
    <div class="brand-name">VERDANET</div>
    <div class="tagline">IT SOLUTIONS FOR SMALL BUSINESS</div>
    <div class="website">www.verdanet.com</div>
  </section>

  <section class="card card--back" aria-label="Card back">
    <svg class="corner-shape" width="579" height="354" viewBox="0 0 579 354" aria-hidden="true">
      <circle cx="480" cy="360" r="240" fill="var(--brand-green)"/>
    </svg>
    <div class="brand-name">VERDANET</div>
    <div class="tagline">IT SOLUTIONS FOR SMALL BUSINESS</div>

    <address class="address" style="font-style:normal">Elm Road, Redcliffe<br>QLD 4020</address>

    <ul class="contact-list">
      <li>
        <svg viewBox="0 0 16 16" aria-hidden="true"><path fill="var(--brand-green)" d="M3.6 1.2l2.3 2.6-1.3 1.8c.9 2 2.6 3.7 4.6 4.6l1.8-1.3 2.6 2.3-1.4 2.3C6.5 15 1 9.5 1.3 2.6z"/></svg>
        07 3490 2175
      </li>
      <li>
        <svg viewBox="0 0 16 16" aria-hidden="true"><rect x="1" y="3" width="14" height="10" fill="none" stroke="var(--brand-green)" stroke-width="1.6"/><path d="M1.5 3.5L8 9l6.5-5.5" fill="none" stroke="var(--brand-green)" stroke-width="1.6"/></svg>
        support@verdanet.com
      </li>
      <li>
        <svg viewBox="0 0 16 16" aria-hidden="true"><g fill="none" stroke="var(--brand-green)" stroke-width="1.4"><circle cx="8" cy="8" r="6.5"/><ellipse cx="8" cy="8" rx="3" ry="6.5"/><path d="M1.5 8h13M2.5 4.8h11M2.5 11.2h11"/></g></svg>
        www.verdanet.com
      </li>
    </ul>

    <div class="person">
      <div class="person__name">Daniel Harper</div>
      <div class="person__role">Founder</div>
    </div>
  </section>
</main>
</body>
</html>
```